GUARANTEED WordPress design needed for a sassy, confident charisma coach!

We need a website design for Mira Haskett's brand new, responsive, Wordpress website.
Mira is a trainer / coach who teaches people how to be more charismatic and runs events, publishes video courses and has an ongoing video blog. Her old website is here: www.mirahaskett-example.co.uk ... but it's now time to have a much better site!
We have a strong idea about the technical components of the website, but we need a designer's eye to create a great style for the site (and provide layered PSD files which our developers will then convert to HTML and CSS).
Mira's brand is sassy, brave, warm and confident. The videos on her existing site give quite a good feel for her personality. We need a clean, stylish and compelling page that isn't too corporate and captures her personality. Every element needs to feel coherent, from fonts and headings to colours and spacing.
The following sites are not exactly what Mira wants (and certainly aren't right in terms of colours) but they give you an idea of the kind of people she is competing against and the area she is operating in:
http://www.fenna-troske.example/
http://brynwellow.example/
Ideally, you will have done something similar and be able to key in on exactly the kind of thing we want: we're not looking to reinvent the wheel. Hopefully you won't mind tweaking a few things if you are close to what we need.
More detail is provided in the word document attached. But in a nutshell we need: a banner, footer, sign-up strap, menu bar, signature and 4 different basic page types. We want bursts of bright colours, contrasted with black and white if possible - sorry we can't be more specific than that...
The word doc also contains some amateur mock-ups as well (the images are also just mockups at this stage) - but although these give a general sense of the structure what we are looking for, we are clearly not designers...so please help! We need a designer's touch!
Kind regards,
Tomas
PS The layered PSD versions of the mockup files are available on Quellbox: https://files.quellbox.example/sh/k27rpw4m1xqzv/QWxnEr8tLpVu3YcMd0aHs?dl=0
Project Deadline Extended Reason: We are looking for a polished, "designed" look. The mock-up that we have provided is just indicative of the features we want. Added Saturday, May 14, 2016
Entrepreneurs who need to sell themselves.
4 page

```html
<!DOCTYPE html>
<html lang="en">
<head>
<meta charset="utf-8">
<title>Mira Haskett – Tips &amp; Videos</title>
<link href="https://fonts.googleapis.com/css2?family=Raleway:wght@400;500;600&display=swap" rel="stylesheet">
<style>
:root{
  --page:#ffffff;
  --panel:#fafafa;
  --ink:#1d1d1d;
  --text:#3a3a3a;
  --accent:#c4000b;
  --rule:#e6e6e6;
  --footer:#151515;
  --photo-warm-a:#b89c78;
  --photo-warm-b:#5d5348;
  --photo-breakfast-a:#d9cbb5;
  --photo-breakfast-b:#6f5a47;
}
*{box-sizing:border-box;margin:0;padding:0}
html,body{width:1200px;height:579px;overflow:hidden;background:var(--page);font-family:"Raleway",Arial,sans-serif;color:var(--ink)}
.page{position:relative;width:1200px;height:579px}

.sidebar{position:absolute;left:181px;top:0;width:187px;height:516px;background:var(--panel);text-align:center}
.brand{position:absolute;top:62px;left:0;width:100%;font-size:20px;font-weight:500;color:var(--ink);letter-spacing:.5px}
.main-nav{position:absolute;top:127px;left:34px;width:119px;list-style:none}
.main-nav li{height:28px;line-height:28px;font-size:10px;border-bottom:1px solid var(--rule)}
.main-nav li:last-child{border-bottom:none}
.main-nav a{color:var(--ink);text-decoration:none}
.main-nav .current a{color:var(--accent)}
.social{position:absolute;top:355px;left:20px;width:147px;padding:8px 0;border-top:1px solid var(--rule);border-bottom:1px solid var(--rule);display:flex;justify-content:center;gap:3px}
.social span{position:relative;width:22px;height:22px;border:1.5px solid var(--ink);border-radius:50%}
.social span::after{content:"";position:absolute;left:50%;top:50%;width:7px;height:7px;margin:-3.5px 0 0 -3.5px;border-radius:50%;background:var(--ink)}
.social span.active{border-color:var(--accent)}
.social span.active::after{background:var(--accent)}
.sidebar-credit{position:absolute;top:429px;left:0;width:100%;font-size:10px;line-height:13px}

.card{position:absolute;width:190px;height:250px;background:var(--panel);text-align:center}
.card .photo{display:block;width:190px;height:131px}
.card h2{font-size:10.4px;font-weight:600;line-height:13px;padding:0 8px;white-space:nowrap}
.card p{font-size:8.7px;line-height:12.4px;color:var(--text);padding:0 20px}
.card.with-photo h2{margin-top:9px}
.card.with-photo p{margin-top:9px}
.card.text-only h2{margin-top:41px;white-space:normal;padding:0 14px}
.card.text-only p{margin-top:19px;padding:0 14px;hyphens:auto}
.read-more{position:absolute;left:50px;top:211px;width:90px;height:19px;line-height:19px;background:var(--accent);color:#fff;font-size:8.7px;text-decoration:none}

.col-1{left:389px}.col-2{left:599px}.col-3{left:808px}
.row-1{top:0}.row-2{top:266px}
.card.offset h2{margin-top:16px}
.card.offset p{margin-top:3px}

.site-footer{position:absolute;left:0;top:544px;width:1200px;height:35px;background:var(--footer);color:#fff;font-size:10.5px;line-height:35px;text-align:center}
</style>
</head>
<body>
<div class="page">
  <aside class="sidebar">
    <div class="brand">Mira Haskett</div>
    <ul class="main-nav">
      <li><a href="#">Home</a></li>
      <li class="current"><a href="#">Tips &amp; Videos</a></li>
      <li><a href="#">Individual</a></li>
      <li><a href="#">Business</a></li>
      <li><a href="#">Success Stories</a></li>
      <li><a href="#">Questions?</a></li>
      <li><a href="#">Contact</a></li>
    </ul>
    <div class="social" aria-label="Social links">
      <span></span><span></span><span></span><span></span><span class="active"></span><span></span>
    </div>
    <p class="sidebar-credit">© 2016 mirahaskett</p>
  </aside>

  <article class="card with-photo col-1 row-1">
    <svg class="photo" role="img" aria-label="Photo of a tied bundle of old letters with a pen"><defs><linearGradient id="g1" x1="0" y1="0" x2="1" y2="1"><stop offset="0" stop-color="var(--photo-warm-a)"/><stop offset="1" stop-color="var(--photo-warm-b)"/></linearGradient></defs><rect width="190" height="131" fill="url(#g1)"/></svg>
    <h2>Driving in the City</h2>
    <p>Driving in the city is a very important skill, especially if you happen to live there.</p>
    <a class="read-more" href="#">Read More</a>
  </article>

  <article class="card text-only col-2 row-1">
    <h2>Are you a cultured international traveler</h2>
    <p>There are many variations of passages of Lorem Ipsum available, but the majority have suffered alteration in some form, by injected humour, or randomised words which don't look even slightly believable. If you are going to use a passage of Lorem Ipsum.</p>
    <a class="read-more" href="#">Read More</a>
  </article>

  <article class="card with-photo offset col-3 row-1">
    <svg class="photo" role="img" aria-label="Photo of croissants and a coffee bag on a table"><defs><linearGradient id="g2" x1="0" y1="0" x2="1" y2="1"><stop offset="0" stop-color="var(--photo-breakfast-a)"/><stop offset="1" stop-color="var(--photo-breakfast-b)"/></linearGradient></defs><rect width="190" height="131" fill="url(#g2)"/></svg>
    <h2>A good real estate investment</h2>
    <p>Driving in the city is a very important skill, especially if you happen to live there.</p>
    <a class="read-more" href="#">Read More</a>
  </article>

  <article class="card text-only col-1 row-2">
    <h2>Are you a cultured international traveler</h2>
    <p>There are many variations of passages of Lorem Ipsum available, but the majority have suffered alteration in some form, by injected humour, or randomised words which don't look even slightly believable. If you are going to use a passage of Lorem Ipsum.</p>
    <a class="read-more" href="#">Read More</a>
  </article>

  <article class="card with-photo col-2 row-2">
    <svg class="photo" role="img" aria-label="Photo of a tied bundle of old letters with a pen"><rect width="190" height="131" fill="url(#g1)"/></svg>
    <h2>Driving in the City</h2>
    <p>Driving in the city is a very important skill, especially if you happen to live there.</p>
    <a class="read-more" href="#">Read More</a>
  </article>

  <article class="card with-photo offset col-3 row-2">
    <svg class="photo" role="img" aria-label="Photo of croissants and a coffee bag on a table"><rect width="190" height="131" fill="url(#g2)"/></svg>
    <h2>A good real estate investment</h2>
    <p>Driving in the city is a very important skill, especially if you happen to live there.</p>
    <a class="read-more" href="#">Read More</a>
  </article>

  <footer class="site-footer">All rights reserved © 2016 mirahaskett</footer>
</div>
</body>
</html>
```